National Intensive Course Provider needs an advert designed to appear in trams

We need an advertisement designed to put in trams, the dimensions are 660mm wide and 203mm height. We offer intensive driving courses all over the UK, allowing pupils to complete a full driving course within a week/two weeks with both the theory and practical tests included in the course (as required). We would like the colours used to be green and dark blue, maybe red also, whatever looks best from them colours really.

Key Points to highlight:
- Pass your driving test within 1 week
- Start your course as early as next week
- Both tests included as part of your course (if required)

I have attached some images which could be included in the design

```html
<!DOCTYPE html>
<html lang="en">
<head>
<meta charset="utf-8">
<title>Learn to Drive – Tram Advert</title>
<link href="https://fonts.googleapis.com/css2?family=Michroma&family=Lexend:wght@400;500;600&display=swap" rel="stylesheet">
<style>
  :root{
    --backdrop:#535353;
    --white:#ffffff;
    --green:#19d11e;
    --green-bright:#2ee82b;
    --navy:#05195e;
    --ink:#111111;
    --red:#d0161c;
    --photo-top:#5b7b3a;
    --photo-bottom:#b8232a;
  }
  *{margin:0;padding:0;box-sizing:border-box}
  html,body{width:1200px;height:1200px;overflow:hidden;background:var(--backdrop)}
  .advert{
    position:absolute;left:49px;top:431px;width:1102px;height:338px;
    background:var(--white);overflow:hidden;
    font-family:"Lexend",sans-serif;
  }
  .advert-shapes{position:absolute;inset:0;width:100%;height:100%}
  .headline{
    position:absolute;left:527px;top:34px;
    font-family:"Michroma",sans-serif;font-size:40px;line-height:1;
    color:var(--green);letter-spacing:4px;-webkit-text-stroke:1.2px var(--green);
    white-space:nowrap;
  }
  .benefits{position:absolute;left:540px;top:87px;list-style:none}
  .benefits li{
    position:relative;padding-left:29px;white-space:nowrap;
    font-size:22px;font-weight:600;color:var(--ink);line-height:33.5px;
  }
  .benefits li svg{position:absolute;left:0;top:9px;width:20px;height:16px}
  .benefits .note{display:block;line-height:24px;margin-top:-4px}
  .discount{
    position:absolute;left:495px;top:215px;white-space:nowrap;
    font-size:25.5px;font-weight:600;color:var(--green);
  }
  .contact-lead{
    position:absolute;left:498px;top:263px;white-space:nowrap;
    font-size:17.5px;font-weight:500;color:var(--white);
  }
  .contact-row{
    position:absolute;left:509px;top:296px;display:flex;gap:30px;white-space:nowrap;
    font-size:17.5px;font-weight:500;color:var(--white);
  }
  .contact-row span{display:flex;align-items:center;gap:5px}
  .contact-row svg{width:12px;height:14px}
  .brand{
    position:absolute;left:925px;top:209px;width:148px;height:109px;
    background:var(--navy);border:2px solid var(--red);border-radius:16px;
    display:flex;align-items:center;justify-content:center;gap:8px;padding:0 10px;
    font-size:17px;font-weight:600;color:var(--white);line-height:1.2;text-align:left;
  }
  .brand-mark{flex:none;width:12px;height:12px;background:var(--red)}
  .badge-text{
    position:absolute;left:351px;top:53px;width:120px;text-align:center;
    font-family:"Michroma",sans-serif;font-size:16.5px;line-height:26px;
    color:var(--ink);-webkit-text-stroke:0.6px var(--ink);
  }
</style>
</head>
<body>
  <section class="advert">
    <svg class="advert-shapes" viewBox="0 0 1102 338">
      <defs>
        <linearGradient id="photoTone" x1="0" y1="0" x2="0" y2="1">
          <stop offset="0" stop-color="var(--photo-top)"/>
          <stop offset="0.45" stop-color="#6d7050"/>
          <stop offset="1" stop-color="var(--photo-bottom)"/>
        </linearGradient>
      </defs>
      <polygon class="photo-area" role="img" aria-label="Photo of a smiling new driver holding his pass certificate beside a red learner car, trees behind"
        points="0,0 368,0 455,164 384,338 0,338" fill="url(#photoTone)"/>
      <polygon class="chevron-navy" points="372,0 398,0 484,164 416,338 388,338 460,164" fill="var(--navy)"/>
      <polygon class="chevron-green" points="398,0 420,0 506,164 440,338 418,338 488,164" fill="var(--green)"/>
      <polygon class="contact-band" points="474,254 1102,254 1102,338 440,338" fill="var(--navy)"/>
      <g class="price-badge" transform="translate(410 78)" fill="var(--green-bright)" stroke="#0a5e0a" stroke-width="0.8">
        <rect x="-47" y="-47" width="94" height="94"/>
        <rect x="-47" y="-47" width="94" height="94" transform="rotate(15)"/>
        <rect x="-47" y="-47" width="94" height="94" transform="rotate(30)"/>
        <rect x="-47" y="-47" width="94" height="94" transform="rotate(45)"/>
        <rect x="-47" y="-47" width="94" height="94" transform="rotate(60)"/>
        <rect x="-47" y="-47" width="94" height="94" transform="rotate(75)"/>
        <circle r="58" stroke="none"/>
      </g>
    </svg>

    <div class="badge-text">ONLY<br>PRICE!!</div>

    <h1 class="headline">LEARN TO DRIVE</h1>

    <ul class="benefits">
      <li><svg viewBox="0 0 20 16"><rect x="1" y="3" width="12" height="12" fill="none" stroke="var(--green)" stroke-width="2"/><path d="M4 8l4 4 10-11" fill="none" stroke="var(--green)" stroke-width="2.6"/></svg>Pass your driving test within 1 week</li>
      <li><svg viewBox="0 0 20 16"><rect x="1" y="3" width="12" height="12" fill="none" stroke="var(--green)" stroke-width="2"/><path d="M4 8l4 4 10-11" fill="none" stroke="var(--green)" stroke-width="2.6"/></svg>Start your course as early as next week</li>
      <li><svg viewBox="0 0 20 16"><rect x="1" y="3" width="12" height="12" fill="none" stroke="var(--green)" stroke-width="2"/><path d="M4 8l4 4 10-11" fill="none" stroke="var(--green)" stroke-width="2.6"/></svg>Both tests included as part of your course<span class="note">(if required)</span></li>
    </ul>

    <p class="discount">Ask for your discount Package!!</p>

    <p class="contact-lead">For more information Contact us today!!</p>
    <div class="contact-row">
      <span><svg viewBox="0 0 12 14"><path d="M3 1l2 3-1.5 1.5c.6 2 1.8 3.5 3.5 4.5L8.5 8.5l3 2-1 2.5C6 13 2 8 1.5 2.5z" fill="var(--green)"/></svg>123-456-7890</span>
      <span><svg viewBox="0 0 14 14"><rect x="0.5" y="3" width="13" height="9" fill="var(--green)"/><path d="M0.5 3l6.5 5 6.5-5" fill="none" stroke="var(--navy)" stroke-width="1.2"/></svg>info@companyname.com</span>
    </div>

    <div class="brand"><span class="brand-mark"></span><span>Kestrel<br>Driving<br>Courses</span></div>
  </section>
</body>
</html>
```